Stationary for Keeping Steady

we are in the process of creating a more professional image for our company Keeping Steady Paramedical Services. We have recently had a new logo and general brochure designed using artpitchhub and have been impressed by the quality of submissions.

We need:
- Letterhead (A4)
- Business Cards
- With compliments slips
- Email stationary

Letterhead information:
Address - 47 Wattlebrook Drive, Fernhollow Vic 3091
Phone - 1800 462 817
email - enquiries@keepsteady.com.au
Internet - www.keepsteady.com.au
ABN - 82 463 915 207
ACN - 264 871 035

Files need to be able to be edited in Illustrator CS2

Business Cards / with compliments slips / email stationary:
Double sided.
One side to have Name, Mobile number, company phone 1800462817, email, internet address

Files need to be able to be edited in Illustrator CS2 (except email stationary)

Our website is www.keepsteady.com.au for more information. Do not base designs on the website as it will eventually be revised.

Target Market(s)

Australian based businesses, government departments and schools. We specialise in corporate customers rather than public first aid course

Industry/Entity Type

Internet

Requirements
Must have
• Where applicable file to be editable in illustrator CS2 to allow future alterations.

```html
<!DOCTYPE html>
<html lang="en">
<head>
<meta charset="utf-8">
<title>Keeping Steady Paramedical Services – Stationery</title>
<link rel="stylesheet" href="https://fonts.googleapis.com/css2?family=Questrial&family=Arimo:wght@700&display=swap">
<style>
  :root{
    --bg:#1c1c1e;
    --paper:#ffffff;
    --red:#c1262c;
    --red-dark:#8a1217;
    --ink:#1b1b1b;
    --ink-soft:#5a5a5a;
    --grey:#8a8a8a;
    --grey-light:#b5b5b5;
  }
  *{box-sizing:border-box;margin:0;padding:0}
  html,body{width:909px;height:1200px;overflow:hidden;background:var(--bg)}
  body{position:relative;font-family:"Questrial",sans-serif;color:var(--ink)}
  .gradients{position:absolute;width:0;height:0}
  .sheet{position:absolute;background:var(--paper);overflow:hidden}
  .band{position:absolute;left:0;display:block}
  .brand{position:absolute;display:flex;align-items:center;gap:6px;
    font-family:"Arimo",sans-serif;font-weight:700;color:var(--red);white-space:nowrap}
  .brand-mark{display:block;flex:none;background:var(--red)}
  .brand-name{display:flex;flex-direction:column;line-height:1.05}
  .brand-sub{font-size:.56em}
  .contact{position:absolute;text-align:right;color:var(--grey);line-height:1.32;letter-spacing:.2px}

  /* Letterhead */
  .letterhead{left:30px;top:30px;width:440px;height:622px}
  .letterhead .band{top:52px}
  .letterhead .brand{left:118px;top:78px;font-size:14px}
  .letterhead .brand-mark{width:12px;height:12px}
  .letterhead .contact{right:26px;top:122px;font-size:8px}

  /* Compliments slip */
  .slip{left:500px;top:30px;width:379px;height:179px}
  .slip .band{top:26px}
  .slip .brand{left:102px;top:52px;font-size:13px}
  .slip .brand-mark{width:11px;height:11px}
  .slip .contact{right:18px;top:98px;font-size:8px}

  /* Business card front */
  .card-front{left:525px;top:240px;width:330px;height:201px}
  .card-front .brand{left:0;right:0;top:36px;justify-content:center;font-size:12px}
  .card-front .brand-mark{width:10px;height:10px}
  .card-front .person{position:absolute;right:178px;top:98px;text-align:right;font-size:8px;line-height:1.35;color:var(--ink-soft)}
  .card-front .person .name{color:var(--ink)}
  .card-front .divider{position:absolute;left:161px;top:98px;width:1px;height:62px;background:var(--grey-light)}
  .card-front .details{position:absolute;left:170px;top:98px;font-size:8px;line-height:1.35;color:var(--grey)}

  /* Business card back */
  .card-back{left:525px;top:460px;width:330px;height:201px;
    background:linear-gradient(180deg,var(--red) 0%,var(--red-dark) 100%)}
  .card-back .band{top:60px}
  .card-back .brand{left:84px;top:74px;font-size:13px}
  .card-back .brand-mark{width:11px;height:11px}

  /* Email stationery */
  .email{left:30px;top:700px;width:849px;height:250px}
  .email .greeting{position:absolute;left:36px;top:170px;font-size:10px;line-height:1.3;color:var(--ink-soft)}
  .email .greeting .small{font-size:8px;color:var(--grey)}
  .email .signature-bar{position:absolute;left:12px;top:168px;width:16px;height:40px;background:linear-gradient(180deg,var(--red),var(--red-dark))}
  .email .band{left:240px;top:160px}
  .email .brand{left:478px;top:172px;font-size:19px}
  .email .brand-mark{width:15px;height:15px}
</style>
</head>
<body>

<svg class="gradients" width="0" height="0" aria-hidden="true">
  <defs>
    <linearGradient id="redGrad" x1="0" y1="0" x2="0" y2="1">
      <stop offset="0" stop-color="#d0383c"/>
      <stop offset="1" stop-color="#8a1217"/>
    </linearGradient>
    <linearGradient id="darkGrad" x1="0" y1="0" x2="0" y2="1">
      <stop offset="0" stop-color="#0f0f10"/>
      <stop offset="1" stop-color="#5c5c5e"/>
    </linearGradient>
  </defs>
</svg>

<!-- Letterhead -->
<section class="sheet letterhead" aria-label="Letterhead">
  <svg class="band" width="440" height="70" viewBox="0 0 440 70">
    <path d="M0 26 L96 26 C88 36 94 52 112 54 L0 54 Z" fill="url(#redGrad)"/>
    <path d="M262 58 C282 58 280 26 304 20 L440 6 L440 40 L330 44 C306 46 298 58 262 58 Z" fill="url(#darkGrad)"/>
  </svg>
  <div class="brand"><span class="brand-mark"></span><span class="brand-name"><span>Keeping Steady</span><span class="brand-sub">Paramedical Services</span></span></div>
  <div class="contact">
    Address - 47 Wattlebrook Drive, Fernhollow Vic 3091<br>
    Phone - 1800 462 817<br>
    email - enquiries@keepsteady.com.au<br>
    Internet - www.keepsteady.com.au<br>
    ABN - 82 463 915 207<br>
    ACN - 264 871 035
  </div>
</section>

<!-- With compliments slip -->
<section class="sheet slip" aria-label="With compliments slip">
  <svg class="band" width="379" height="70" viewBox="0 0 379 70">
    <path d="M0 30 L82 30 C74 40 80 56 96 58 L0 58 Z" fill="url(#redGrad)"/>
    <path d="M262 58 C280 58 278 22 300 16 L379 4 L379 38 L318 42 C298 44 292 58 262 58 Z" fill="url(#darkGrad)"/>
  </svg>
  <div class="brand"><span class="brand-mark"></span><span class="brand-name"><span>Keeping Steady</span><span class="brand-sub">Paramedical Services</span></span></div>
  <div class="contact">
    Address - 47 Wattlebrook Drive, Fernhollow Vic 3091<br>
    Phone - 1800 462 817<br>
    email - enquiries@keepsteady.com.au<br>
    Internet - www.keepsteady.com.au<br>
    ABN - 82 463 915 207<br>
    ACN - 264 871 035
  </div>
</section>

<!-- Business card, front -->
<section class="sheet card-front" aria-label="Business card front">
  <div class="brand"><span class="brand-mark"></span><span class="brand-name"><span>Keeping Steady</span><span class="brand-sub">Paramedical Services</span></span></div>
  <div class="person">
    <span class="name">Daniel Marsh</span><br>
    SEO<br>
    Phone - 1800 462 899
  </div>
  <div class="divider"></div>
  <div class="details">
    47 Wattlebrook Drive,<br>
    Fernhollow Vic 3091<br>
    enquiries@keepsteady.com.au<br>
    www.keepsteady.com.au<br>
    ABN - 82 463 915 207<br>
    ACN - 264 871 035
  </div>
</section>

<!-- Business card, back -->
<section class="sheet card-back" aria-label="Business card back">
  <svg class="band" width="330" height="60" viewBox="0 0 330 60">
    <path d="M0 12 L300 12 C316 12 316 2 330 0 C322 14 320 40 300 44 L0 44 Z" fill="#ffffff"/>
  </svg>
  <div class="brand"><span class="brand-mark"></span><span class="brand-name"><span>Keeping Steady</span><span class="brand-sub">Paramedical Services</span></span></div>
</section>

<!-- Email stationery -->
<section class="sheet email" aria-label="Email stationery">
  <div class="signature-bar"></div>
  <div class="greeting">
    Greetings<br>
    Daniel Marsh<br>
    SEO - Phone - 1800 462 899<br>
    <span class="small">Fernhollow Vic 3091 - www.keepsteady.com.au</span>
  </div>
  <svg class="band" width="609" height="56" viewBox="0 0 609 56">
    <path d="M0 14 L236 14 C226 26 234 44 256 46 L0 46 Z" fill="url(#redGrad)"/>
    <path d="M486 50 C506 50 504 14 530 8 L609 2 L609 32 L550 36 C528 38 522 50 486 50 Z" fill="url(#darkGrad)"/>
  </svg>
  <div class="brand"><span class="brand-mark"></span><span class="brand-name"><span>Keeping Steady</span><span class="brand-sub">Paramedical Services</span></span></div>
</section>

</body>
</html>
```